Carrowell Business Card Re-design

Our current cards are outdated. This is our website www.carrowellinsights.example. We would like something that is "on-brand" and consistent with our social media sites. We are strategic consultants with a core competency in Marketing Research. Although, please know we are considering a brand logo redesign and potentially a new look. If we like your work here we will invite you to participate when we get to that project. Thank you very much. Harriet
Here are our social sites: https://twitter.com/Carrowell?lang=en
https://plus.google.com/+Carrowellinsights
https://www.linkedin.com/company/5094827/
https://www.facebook.com/CarrowellInc/
Business

```html
<!DOCTYPE html>
<html lang="en">
<head>
<meta charset="utf-8">
<title>Carrowell Business Card</title>
<link href="https://fonts.googleapis.com/css2?family=Arimo:wght@400;700&display=swap" rel="stylesheet">
<style>
  :root {
    --paper: #efefef;
    --card-white: #f6f6f4;
    --brand-green: #8aab4c;
    --brand-green-deep: #7d9c44;
    --brand-blue: #46709e;
    --ink-white: #ffffff;
    --ink-dark: #2b2b2b;
  }
  * { box-sizing: border-box; margin: 0; padding: 0; }
  html, body {
    width: 1200px; height: 1000px; overflow: hidden;
    background: var(--paper);
    font-family: "Arimo", Arial, sans-serif;
  }
  .canvas { position: relative; width: 1200px; height: 1000px; }
  .card {
    position: absolute; left: 250px; width: 700px; height: 400px;
    overflow: hidden;
    box-shadow: 0 6px 18px rgba(0,0,0,0.12);
  }
  .card-back { top: 70px; }
  .card-front { top: 530px; }
  .card-shapes { position: absolute; inset: 0; width: 700px; height: 400px; }

  .back-brand {
    position: absolute; left: 350px; top: 200px;
    transform: translate(-50%, -50%) rotate(-33deg);
    text-align: center; color: var(--ink-white);
    white-space: nowrap;
  }
  .back-brand .wordmark {
    display: block; font-weight: 700; font-size: 128px;
    letter-spacing: -2px; line-height: 1;
  }
  .back-brand .web {
    display: block; font-size: 26px; margin-top: 4px; letter-spacing: 0.5px;
  }

  .front-brand {
    position: absolute; left: 160px; top: 120px;
    transform: translate(-50%, -50%) rotate(-39.8deg);
    font-weight: 700; font-size: 66px; letter-spacing: -1px;
    color: var(--brand-green-deep); white-space: nowrap; line-height: 1;
  }

  .contact-block {
    position: absolute; left: 400px; top: 120px; width: 270px;
    color: var(--ink-white);
  }
  .person-name {
    font-weight: 700; font-size: 30px; letter-spacing: 0.3px;
    padding-bottom: 6px; border-bottom: 2px solid var(--ink-white);
    white-space: nowrap;
  }
  .person-name .surname { color: var(--brand-blue); }
  .person-role { font-size: 19px; margin-top: 8px; letter-spacing: 0.3px; }
  .contact-list { list-style: none; margin-top: 28px; }
  .contact-list li {
    display: flex; align-items: center; gap: 14px;
    font-size: 17px; height: 36px; white-space: nowrap;
  }
  .contact-list svg { width: 24px; height: 24px; flex: none; }
</style>
</head>
<body>
<main class="canvas">

  <section class="card card-back" aria-label="Card back">
    <svg class="card-shapes" viewBox="0 0 700 400" aria-hidden="true">
      <rect width="700" height="400" fill="var(--brand-green)"/>
      <polygon points="0,0 250,0 0,250" fill="var(--brand-blue)"/>
      <polygon points="700,110 700,400 540,400" fill="var(--brand-blue)"/>
    </svg>
    <div class="back-brand">
      <span class="wordmark">carrowell</span>
      <span class="web">www.carrowellinsights.example</span>
    </div>
  </section>

  <section class="card card-front" aria-label="Card front">
    <svg class="card-shapes" viewBox="0 0 700 400" aria-hidden="true">
      <rect width="700" height="400" fill="var(--brand-green-deep)"/>
      <polygon points="0,0 360,0 0,300" fill="var(--card-white)"/>
      <polygon points="0,300 150,175 290,400 0,400" fill="var(--brand-blue)"/>
    </svg>
    <div class="front-brand">carrowell</div>

    <div class="contact-block">
      <h1 class="person-name">Harriet <span class="surname">Pembrook</span></h1>
      <p class="person-role">Marketing Researcher</p>
      <ul class="contact-list">
        <li>
          <svg viewBox="0 0 24 24" aria-hidden="true"><rect x="6" y="1" width="12" height="22" rx="2" fill="var(--ink-dark)"/><rect x="8" y="4" width="8" height="14" fill="var(--ink-white)"/></svg>
          <span>+1-555-014-2290</span>
        </li>
        <li>
          <svg viewBox="0 0 24 24" aria-hidden="true"><rect x="1" y="5" width="22" height="15" fill="var(--ink-dark)"/><polyline points="1,5 12,14 23,5" fill="none" stroke="var(--brand-green-deep)" stroke-width="1.6"/></svg>
          <span>info@carrowellinsights.example</span>
        </li>
        <li>
          <svg viewBox="0 0 24 24" aria-hidden="true"><circle cx="12" cy="12" r="11" fill="var(--ink-white)" stroke="var(--ink-dark)" stroke-width="1.5"/><g fill="none" stroke="var(--ink-dark)" stroke-width="1.2"><ellipse cx="12" cy="12" rx="5" ry="11"/><line x1="12" y1="1" x2="12" y2="23"/><line x1="1" y1="12" x2="23" y2="12"/><line x1="3" y1="7" x2="21" y2="7"/><line x1="3" y1="17" x2="21" y2="17"/></g></svg>
          <span>www.carrowellinsights.example</span>
        </li>
      </ul>
    </div>
  </section>

</main>
</body>
</html>
```